BrightNook Software (a new software house) needs a Wordpress web site

We need a Wordpress web site. We develop innovative software as a service (on demand) for companies and cunsumers.
Updates

Reason: I need extra days to analyze.

Target Market(s)

Consumers who use mobile software to access useful information about your day by day in a crowd plataform and on demand.

Industry/Entity Type

Software

Requirements
Must have
• See wordpress template suggestion:
http://themes.plinvoa.com/?theme=marmot

```html
<!DOCTYPE html>
<html lang="en">
<head>
<meta charset="utf-8">
<title>BrightNook Software</title>
<link href="https://fonts.googleapis.com/css2?family=Open+Sans:wght@300;400;600&family=Roboto+Condensed:wght@400;700&display=swap" rel="stylesheet">
<style>
:root{
  --ink:#2c2c34;
  --text:#5b5b63;
  --brand:#3d5199;
  --brand-soft:#6a7bb5;
  --navy:#2b3a7e;
  --hero-top:#7f8fcb;
  --hero-bottom:#586dae;
  --nav-bg:#e9ecf4;
  --caption:#7c8fcb;
  --social:#8e9bd0;
  --footer:#3a3a3c;
  --footer-line:#c9c9cc;
  --white:#ffffff;
}
*{margin:0;padding:0;box-sizing:border-box}
html,body{width:765px;height:1200px;overflow:hidden;background:var(--white)}
body{position:relative;font-family:"Open Sans",Arial,sans-serif;color:var(--text)}
.abs{position:absolute}
.top-rule{left:0;top:0;width:765px;height:3px;background:var(--ink)}
.brand{left:272px;top:28px;display:flex;align-items:center;gap:10px}
.brand-mark{width:34px;height:34px;border-radius:50%;background:var(--navy)}
.brand-name{font-size:22px;font-weight:600;color:var(--navy);letter-spacing:.2px}
.social{top:54px;left:622px;display:flex;gap:3px}
.social span{width:20px;height:20px;border-radius:50%;background:var(--social)}
.nav{left:0;top:86px;width:765px;height:35px;background:var(--nav-bg);border-top:1px solid #dde1ec;display:flex;justify-content:center;align-items:center}
.nav a{font-family:"Roboto Condensed",Arial,sans-serif;font-size:11px;font-weight:700;color:var(--ink);text-decoration:none;letter-spacing:.4px;padding:0 15px;border-left:1px solid #9aa0b8;line-height:11px}
.nav a:first-child{border-left:0}
.hero{left:0;top:121px;width:765px;height:265px;background:linear-gradient(180deg,var(--hero-top),var(--hero-bottom))}
.hero-kicker{left:69px;top:45px;font-size:23px;font-weight:300;color:#dfe4f6}
.hero-title{left:68px;top:68px;font-size:34px;font-weight:400;color:var(--white);letter-spacing:.2px}
.hero-copy{left:69px;top:108px;width:260px;font-size:8.5px;line-height:14.5px;color:#e3e7f6}
.hero-btn{left:70px;top:159px;width:80px;height:27px;background:var(--navy);border-radius:2px;color:var(--white);font-size:11.5px;display:flex;align-items:center;justify-content:center;box-shadow:0 1px 2px rgba(0,0,0,.3)}
.hero-dots{left:71px;top:204px;display:flex;gap:3px}
.hero-dots span{width:9px;height:9px;border-radius:50%;background:#a9b4df}
.hero-dots span:first-child{background:var(--white)}
.hero-art{left:456px;top:36px;width:216px;height:152px;border-radius:10px;background:linear-gradient(135deg,#3a3d4a,#1f2129);box-shadow:0 6px 10px rgba(0,0,0,.25)}
.hero-art::after{content:"";position:absolute;left:18px;top:14px;right:18px;bottom:18px;border-radius:4px;background:linear-gradient(135deg,#f3a23c,#e4532a 55%,#f1efe9)}
.intro-title{left:0;top:410px;width:765px;text-align:center;font-size:22px;color:var(--brand)}
.intro-sub{left:0;top:440px;width:765px;text-align:center;font-size:14px;font-weight:300;color:var(--brand-soft)}
.service{top:484px;width:150px}
.service-head{display:flex;align-items:center;gap:6px;height:28px}
.service-head svg{flex:none}
.service-title{font-size:14.5px;color:var(--ink);font-weight:400}
.service p{margin-top:6px;font-size:8.3px;line-height:13.7px}
.service a{display:block;margin-top:3px;font-size:8.5px;color:var(--brand);text-decoration:none}
.divider{left:46px;width:672px;height:18px;background:radial-gradient(ellipse at top,rgba(0,0,0,.07),rgba(0,0,0,0) 70%)}
.section-title{left:50px;font-size:16.5px;color:var(--ink)}
.project{top:671px;width:202px}
.project-img{width:202px;height:97px}
.project h3{margin-top:8px;font-size:11px;font-weight:400;color:var(--ink)}
.project p{margin-top:2px;font-size:8.3px;line-height:14px}
.post{top:906px;width:202px}
.post-img{width:202px;height:87px}
.post-caption{height:32px;background:var(--caption);color:var(--white);font-family:"Roboto Condensed",Arial,sans-serif;font-size:12px;padding-left:14px;display:flex;align-items:center}
.footer-line{left:0;top:1078px;width:765px;height:6px;background:var(--footer-line)}
.footer{left:0;top:1084px;width:765px;height:116px;background:var(--footer)}
.footer-nav{left:0;top:28px;width:765px;display:flex;justify-content:center}
.footer-nav a{font-size:12px;color:var(--white);text-decoration:none;padding:0 12px;border-left:1px solid #6b6b70;line-height:12px}
.footer-nav a:first-child{border-left:0}
.copyright{left:0;top:56px;width:765px;text-align:center;font-size:9px;color:#b3b3b8}
</style>
</head>
<body>
<div class="abs top-rule"></div>

<header>
  <div class="abs brand"><span class="brand-mark"></span><span class="brand-name">BrightNook Software</span></div>
  <div class="abs social"><span></span><span></span><span></span><span></span></div>
</header>

<nav class="abs nav">
  <a>HOME</a><a>ABOUT US</a><a>SERVICES</a><a>SOFTWARE</a><a>PROJECT</a><a>BLOG</a><a>CONTACT</a>
</nav>

<section class="abs hero">
  <div class="abs hero-kicker">We Provide Customers</div>
  <h1 class="abs hero-title">Innovative Software</h1>
  <p class="abs hero-copy">Mauris vel lacus vitae felis vestibulum volutpat. Etiam est nunc, venenatis in, tristique eu, imperdiet ac, nisl. Cum sociis natoque penatibus et magnis</p>
  <div class="abs hero-btn">Buy Now</div>
  <div class="abs hero-dots"><span></span><span></span><span></span><span></span></div>
  <div class="abs hero-art" role="img" aria-label="Tablet showing colourful business charts and a spreadsheet with a pencil"></div>
</section>

<h2 class="abs intro-title">Aliquam vehicula mi at mauris Maecenas placerat</h2>
<div class="abs intro-sub">nisl at consequat rhoncus, sem nunc</div>

<div class="abs service" style="left:54px">
  <div class="service-head">
    <svg width="24" height="22" viewBox="0 0 24 22"><path d="M9 0h6v8h5l-8 8-8-8h5z" fill="var(--ink)"/><path d="M0 16h3v3h18v-3h3v6H0z" fill="var(--ink)"/></svg>
    <span class="service-title">Featured Service</span>
  </div>
  <p>Nunc tempus felis vitae urna. Vivamus porttitor, g, purus nisi eleifend libero, a tempus libero lectus feugiat felis</p>
  <a>Click here ▸</a>
</div>
<div class="abs service" style="left:226px">
  <div class="service-head">
    <svg width="20" height="24" viewBox="0 0 20 24"><path d="M0 0h13l7 7v17H0z" fill="var(--ink)"/><path d="M4 11h12v2H4zM4 15h12v2H4zM4 19h12v2H4z" fill="#fff"/></svg>
    <span class="service-title">Featured Service</span>
  </div>
  <p>Nunc tempus felis vitae urna. Vivamus porttitor, g, purus nisi eleifend libero, a tempus libero lectus feugiat felis</p>
  <a>Click here ▸</a>
</div>
<div class="abs service" style="left:397px">
  <div class="service-head">
    <svg width="24" height="22" viewBox="0 0 24 22"><rect x="0" y="0" width="24" height="16" rx="1" fill="var(--ink)"/><rect x="2" y="2" width="20" height="11" fill="#fff"/><path d="M9 16h6v3h3v3H6v-3h3z" fill="var(--ink)"/></svg>
    <span class="service-title">Featured Service</span>
  </div>
  <p>Nunc tempus felis vitae urna. Vivamus porttitor, g, purus nisi eleifend libero, a tempus libero lectus feugiat felis</p>
  <a>Click here ▸</a>
</div>
<div class="abs service" style="left:568px">
  <div class="service-head">
    <svg width="30" height="20" viewBox="0 0 30 20"><path d="M7 20a7 7 0 0 1-1-13.9A8 8 0 0 1 21 5a6 6 0 0 1 2 .2A7.5 7.5 0 0 1 23 20z" fill="var(--ink)"/></svg>
    <span class="service-title">Featured Service</span>
  </div>
  <p>Nunc tempus felis vitae urna. Vivamus porttitor, g, purus nisi eleifend libero, a tempus libero lectus feugiat felis</p>
  <a>Click here ▸</a>
</div>

<div class="abs divider" style="top:608px"></div>
<h2 class="abs section-title" style="top:639px;font-weight:400">Latest Projects</h2>

<article class="abs project" style="left:48px">
  <div class="project-img" role="img" aria-label="Colleagues working together at a laptop in a bright office" style="background:linear-gradient(135deg,#e8ecef,#b9c3c9 50%,#8d949a)"></div>
  <h3>Project Tittle</h3>
  <p>Nunc tempus felis vitae urna. Vivamus porttitor, g, purus nisi eleifend libero, a tempus</p>
</article>
<article class="abs project" style="left:278px">
  <div class="project-img" role="img" aria-label="Smiling team member at a computer workstation" style="background:linear-gradient(135deg,#dfe3e6,#b39a86 50%,#5fb7a6)"></div>
  <h3>Project Tittle</h3>
  <p>Nunc tempus felis vitae urna. Vivamus porttitor, g, purus nisi eleifend libero, a tempus</p>
</article>
<article class="abs project" style="left:509px">
  <div class="project-img" role="img" aria-label="Developers reviewing code together on a monitor" style="background:linear-gradient(135deg,#eef0f2,#c8cdd1 50%,#6f6a66)"></div>
  <h3>Project Tittle</h3>
  <p>Nunc tempus felis vitae urna. Vivamus porttitor, g, purus nisi eleifend libero, a tempus</p>
</article>

<div class="abs divider" style="top:844px"></div>
<h2 class="abs section-title" style="top:875px;font-weight:400">Recent Blog Post</h2>

<article class="abs post" style="left:49px">
  <div class="post-img" role="img" aria-label="Hand touching a glowing cloud network of connected devices" style="background:linear-gradient(135deg,#0a2a4c,#0f4f86 55%,#1d7fc0)"></div>
  <div class="post-caption">Phasellus felis dolor</div>
</article>
<article class="abs post" style="left:277px">
  <div class="post-img" role="img" aria-label="Names of programming languages glowing on a blue background" style="background:linear-gradient(135deg,#0a3554,#1678a8 55%,#1aa2cf)"></div>
  <div class="post-caption">Fusce ultricies</div>
</article>
<article class="abs post" style="left:510px">
  <div class="post-img" role="img" aria-label="Blue circuit board pattern with a folder shape" style="background:linear-gradient(135deg,#5b7fc6,#2f63c2 55%,#6aa6e6)"></div>
  <div class="post-caption">Suspendisse vulputate</div>
</article>

<div class="abs footer-line"></div>
<footer class="abs footer">
  <nav class="abs footer-nav"><a>Home</a><a>About Us</a><a>Services</a><a>Software</a><a>Project</a><a>Blog</a><a>Contact</a></nav>
  <div class="abs copyright">Copyright © 2013 Company Name.&nbsp; All right reserved.</div>
</footer>
</body>
</html>
```